Etiquetas para platos preparados de la marca Tarvelia

Necesito el diseño de una belly band o etiquetas para productos cocinados. En ella debe aparecer la siguiente información: el logo de la marca,
Símbolos con la siguiente info: refrigerado entre 2º-4º, pincha el plástico que lo cubre, imagen microondas 3:00, disfruta.
Además necesito que la etiqueta tenga en la parte frontal una zona donde podamos modificar e ir añadiendo el nombre del producto en concreto y en la parte trasera una zona destinada también a los valores nutricionales personalizable.
Por último necesitamos que las etiquetas estén diseñadas en 6 colores diferentes para poder diferenciar entre diferentes categorías (ensaladas, carnes, pescados, postres, ECO...).
Los tamaños de los envases sobre los que debe ir el belly band es el siguiente:
-Formato 1: 180x180x35mm
-Formato 2: 168x128x35mm
-Formato 3: belly band de 30cm de largo

Otro

Target Market(s)

Producto expuesto es vitrinas expositoras de supermercados

Industry/Entity Type

Alimentación

Font styles to use
Sans Serif
Other font styles liked:
• Cocomat y Poppins

Requirements
Must have
• Atractivo visualmente. Fuentes empleadas Cocomat y Montserrat
Nice to have
• Los colores para diferenciar categorías y espacio para poder incluir nosotros el nombre de cada producto. Además un espacio que ponga Origen personalizable también y un logo que ponga casero 100%

```html
<!DOCTYPE html>
<html lang="es">
<head>
<meta charset="utf-8">
<title>Tarvelia – etiqueta belly band pescado</title>
<link rel="stylesheet" href="https://fonts.googleapis.com/css2?family=Poppins:wght@300;400;500;600&family=Josefin+Sans:wght@300;400&display=swap">
<style>
  :root{
    --teal:#7fcfd3;
    --teal-dark:#4fa9ae;
    --kraft:#b48d66;
    --kraft-dark:#8d6a48;
    --ink:#2f2f2f;
    --paper:#ffffff;
    --studio:#e4e4e4;
    --fish-a:#e9e3d4;
    --fish-b:#c9bfa9;
  }
  *{margin:0;padding:0;box-sizing:border-box}
  html,body{width:1200px;height:2392px;overflow:hidden;background:var(--paper)}
  body{position:relative;font-family:"Poppins",sans-serif;color:var(--ink)}
  .category-tag{position:absolute;left:32px;top:140px;width:250px;height:108px;background:var(--teal);
    font-size:34px;font-weight:500;color:var(--paper);padding:30px 0 0 24px}
  .fish-sketch{position:absolute;left:300px;top:150px;width:400px;height:96px;
    background:linear-gradient(90deg,var(--fish-a),var(--fish-b),var(--fish-a));border-radius:48px/30px}
  .font-note{position:absolute;left:32px;top:312px;font-size:22px;font-weight:500;letter-spacing:.5px}
  .proposal{position:absolute;left:32px;top:424px;width:1120px;font-size:23px;line-height:31px;font-weight:300}
  .board{position:absolute;left:0;top:0}
  .band-label{font-family:"Poppins",sans-serif;font-size:38px;font-weight:300;fill:var(--ink)}
  .band-title{font-family:"Poppins",sans-serif;font-size:50px;font-weight:500;fill:var(--ink)}
  .note{font-family:"Poppins",sans-serif;font-size:19px;font-weight:300;fill:var(--ink)}
  .product{font-family:"Josefin Sans",sans-serif;font-size:64px;font-weight:300;fill:var(--teal)}
  .sub{font-family:"Poppins",sans-serif;font-size:13px;letter-spacing:2px;fill:var(--paper)}
  .tiny{font-family:"Poppins",sans-serif;font-size:11px;fill:var(--paper)}
  .tiny-ink{font-family:"Poppins",sans-serif;font-size:11px;fill:var(--ink)}
  .brand{font-family:"Poppins",sans-serif;font-size:22px;font-weight:500;fill:var(--ink)}
  .brand-light{font-family:"Poppins",sans-serif;font-size:18px;font-weight:500;fill:var(--paper)}
  .thanks-band{position:absolute;left:0;top:2172px;width:1200px;height:188px;background:var(--teal)}
  .thanks{position:absolute;left:100px;top:2240px;font-size:40px;font-weight:500;letter-spacing:2px;color:var(--ink)}
</style>
</head>
<body>
  <div class="category-tag">pescado</div>
  <div class="fish-sketch" role="img" aria-label="Ilustración lineal de un pescado"></div>
  <p class="font-note">FUENTE UTILIZADA POPPINS</p>
  <p class="proposal">Propuesta de etiqueta tipo belly band para envases de pescado: diseño moderno y limpio, con ilustración artesanal del producto, colores contrastantes para realzar la marca e información clara sobre conservación y uso.<br>
  Si el diseño les gusta, continuaré con la realización de las otras 5 variantes cambiando la paleta de colores según el tipo de alimento.<br>
  Quedo atenta a sus comentarios.<br>Gracias,<br>Lucía</p>

  <svg class="board" width="1200" height="2392" viewBox="0 0 1200 2392">
    <defs>
      <linearGradient id="fishFill" x1="0" x2="1">
        <stop offset="0" stop-color="#6d8d95"/><stop offset=".5" stop-color="#a9b9b8"/><stop offset="1" stop-color="#6d8d95"/>
      </linearGradient>
      <g id="belly-band">
        <rect class="flap" x="0" y="10" width="50" height="260" fill="none" stroke="#777" stroke-dasharray="6 5"/>
        <rect class="flap" x="950" y="10" width="50" height="260" fill="none" stroke="#777" stroke-dasharray="6 5"/>
        <rect x="50" y="0" width="900" height="280" fill="var(--kraft)"/>
        <!-- back panel -->
        <text class="brand-light" transform="translate(95 200) rotate(-90)">Tarvelia</text>
        <rect x="130" y="30" width="170" height="220" fill="var(--teal)"/>
        <text class="tiny-ink" x="142" y="52">Valores nutricionales</text>
        <g stroke="var(--paper)" stroke-width="1">
          <line x1="140" y1="64" x2="290" y2="64"/><line x1="140" y1="88" x2="290" y2="88"/>
          <line x1="140" y1="112" x2="290" y2="112"/><line x1="140" y1="136" x2="290" y2="136"/>
          <line x1="140" y1="160" x2="290" y2="160"/><line x1="140" y1="184" x2="290" y2="184"/>
        </g>
        <text class="tiny-ink" x="142" y="230">Peso neto 350 g</text>
        <line x1="330" y1="0" x2="330" y2="280" stroke="var(--kraft-dark)"/>
        <!-- front panel -->
        <text class="product" x="362" y="96" textLength="318" lengthAdjust="spacingAndGlyphs">MERLUZA</text>
        <text class="sub" x="366" y="124">CON VERDURA Y ESPECIAS</text>
        <rect x="360" y="140" width="320" height="70" rx="35" fill="url(#fishFill)" role="img" aria-label="Ilustración de una merluza"/>
        <g fill="none" stroke="var(--paper)" stroke-width="2">
          <circle cx="380" cy="240" r="14"/><circle cx="420" cy="240" r="14"/>
          <circle cx="460" cy="240" r="14"/><circle cx="500" cy="240" r="14"/>
        </g>
        <path d="M374 240h12M380 234v12" stroke="var(--paper)" stroke-width="2"/>
        <rect x="413" y="234" width="14" height="11" fill="none" stroke="var(--paper)" stroke-width="2"/>
        <path d="M460 232v8l5 4" fill="none" stroke="var(--paper)" stroke-width="2"/>
        <path d="M494 240l4 5 8-9" fill="none" stroke="var(--paper)" stroke-width="2"/>
        <text class="tiny" x="525" y="236">Refrigerado 2-4°C</text>
        <text class="tiny" x="525" y="252">Microondas 3:00</text>
        <circle cx="655" cy="240" r="22" fill="var(--ink)"/>
        <!-- teal panel -->
        <rect x="700" y="0" width="180" height="280" fill="var(--teal)"/>
        <text class="brand" x="722" y="48">Tarvelia</text>
        <rect x="715" y="80" width="150" height="130" fill="#bfe6e8" role="img" aria-label="Ilustración de pescado en trazo"/>
        <text class="tiny-ink" x="722" y="240">Casero 100%</text>
        <text class="tiny" transform="translate(920 200) rotate(-90)">Origen: Galicia</text>
      </g>
    </defs>

    <!-- template band -->
    <rect x="140" y="790" width="990" height="170" fill="var(--teal)"/>
    <rect x="740" y="760" width="340" height="200" fill="var(--teal)"/>
    <line x1="740" y1="790" x2="740" y2="960" stroke="var(--paper)" stroke-width="2"/>
    <text class="band-label" x="440" y="900">etiqueta central</text>
    <text class="band-title" x="830" y="828">diseño</text>
    <text class="band-title" x="830" y="880">template</text>
    <text class="band-title" x="830" y="932">300x60</text>

    <!-- flat layout -->
    <use href="#belly-band" x="100" y="1060"/>
    <path d="M120 1380v30h20M1080 1380v30h-20" fill="none" stroke="#555" stroke-width="1.5"/>
    <text class="note" x="60" y="1440">alas para pegar la barriga</text>
    <text class="note" x="900" y="1440">alas para pegar la barriga</text>

    <!-- presentation area -->
    <rect x="0" y="1480" width="1200" height="660" fill="var(--studio)"/>
    <use href="#belly-band" transform="translate(130 1660) scale(0.94)"/>
  </svg>

  <div class="thanks-band"></div>
  <p class="thanks">GRACIAS POR VER</p>
</body>
</html>
```